Cleaning Service Company In need of Good Web presence.

The company is a cleaning service company which provides professional staff and service for cleaning. This is a project to build a site that is both solid and a strong recognition of our organization. It is supposed to show quality, cleanliness, professionalism. The use of images and art for imagery is all good just to have a site that is consistent and solid. There might be a chance to make stationary, logo and business cars if someone feels they can build a brand that is consistent. The image we are going for is clean solid and to stand out. Finally stationary should not be expensive to print.

Current logo is attached and can be used or can be made more creative.

Target Market(s)

Corporate and Government entities, that will feel that this company has a brand that sets it apart from the rest. The company is new so the modification of the logo will not be an issue if a more solid brand come out of this project. The idea is to have a clean consistent product that stands our from others in terms of website, stationary, etc

Industry/Entity Type

Cleaning Service

Contact Information for Business Card

P.O.Box 41967
Riffa
Kingdom of Bahrain

Logo Text

Maple Ridge Solutions

Number of Pages Required

4 page

Font styles to use
Sans Serif

Colors
abd036
cadf82
eaf2ce
9bcb3b

Requirements
Must have
• Green Color to be used in order to stick to the name. Also the creativity and boldness in an elegant manner.
Nice to have
• Arabic name of company
• نوفا بلو للحلول ذ.م.م
• if cannot be put at least make a location should be chosen
• Also could be a bit of 3D given to the logo if it could stay elegent.
Should not have
• Should not show people cleaning.

```html
<!DOCTYPE html>
<html lang="en">
<head>
<meta charset="utf-8">
<title>Maple Ridge Solutions – Cleaning Services</title>
<link rel="stylesheet" href="https://fonts.googleapis.com/css2?family=Poppins:wght@300;400;500&family=Open+Sans:ital,wght@0,400;0,600;1,400&display=swap">
<style>
:root{
  --green:#9bcb3b;
  --green-deep:#128a4a;
  --green-soft:#eaf2ce;
  --green-mid:#abd036;
  --red:#ef3f3f;
  --ink:#333;
  --grey:#777;
  --line:#e6e6e6;
  --footer:#1e2024;
  --footer-bar:#18191c;
  --staff-bg:#f6f6f9;
}
*{box-sizing:border-box;margin:0;padding:0}
html,body{width:1200px;height:3035px;overflow:hidden}
body{position:relative;font-family:'Open Sans',sans-serif;color:var(--ink);background:#fff}
h1,h2,h3,h4{font-weight:400}
.abs{position:absolute}
.center{left:0;width:1200px;text-align:center}
.heading{font-family:'Poppins',sans-serif;font-weight:400;font-size:23px;color:var(--ink)}
.heading-rule{width:30px;height:2px;background:var(--green);left:585px}

/* hero */
.hero{top:0;left:0;width:1200px;height:579px;
  background:
    radial-gradient(ellipse 260px 200px at 48% 22%,rgba(150,200,190,.9),rgba(150,200,190,0) 100%),
    radial-gradient(ellipse 120px 140px at 34% 38%,rgba(214,196,60,.75),rgba(214,196,60,0) 100%),
    radial-gradient(ellipse 120px 140px at 70% 36%,rgba(214,196,60,.7),rgba(214,196,60,0) 100%),
    radial-gradient(ellipse 300px 220px at 50% 85%,rgba(40,62,100,.95),rgba(40,62,100,0) 100%),
    linear-gradient(90deg,#5d6a6c 0%,#7d8c8a 30%,#8aa19c 50%,#6c7a7b 75%,#3a4147 100%)}
.hero-shade{left:0;top:0;width:1200px;height:579px;background:rgba(20,30,35,.28)}
.brand{left:91px;top:24px}
.brand-mark{width:94px;height:94px;border-radius:50%;background:var(--green);display:flex;align-items:center;justify-content:center;text-align:center;font-family:'Poppins',sans-serif;font-size:11px;font-weight:500;color:#fff;line-height:1.25;padding:8px}
.nav{top:60px;left:730px;font-family:'Poppins',sans-serif;font-size:12px;color:#fff}
.nav a{color:#fff;text-decoration:none;position:absolute;white-space:nowrap}
.nav a.active{color:var(--green)}
.nav-mark{top:0;left:744px;width:32px;height:3px;background:var(--green)}
.book-btn{left:1010px;top:47px;width:101px;height:42px;background:var(--red);color:#fff;font-family:'Poppins',sans-serif;font-size:12px;display:flex;align-items:center;justify-content:center}
.hero-title{top:230px;font-family:'Poppins',sans-serif;font-weight:500;font-size:33px;line-height:49px;color:#fff}
.hero-btn{left:550px;top:346px;width:101px;height:41px;border:2px solid #fff;color:#fff;font-size:12px;display:flex;align-items:center;justify-content:center}
.slide-dot{left:1153px;width:6px;height:6px;border-radius:50%;background:#fff}

/* process */
.step-circle{width:104px;height:104px;border-radius:50%;border:1px solid #eee;background:#fff;display:flex;align-items:center;justify-content:center}
.step-num{width:24px;height:24px;border-radius:50%;background:var(--green);color:#fff;font-size:11px;display:flex;align-items:center;justify-content:center}
.step-title{width:300px;text-align:center;font-family:'Poppins',sans-serif;font-size:16px;font-weight:400;color:var(--ink)}
.step-text{width:300px;text-align:center;font-size:13px;line-height:18px;color:#555}

/* services */
.services{top:977px;left:0;width:1200px;height:585px;
  background:
    radial-gradient(ellipse 500px 200px at 20% 85%,rgba(40,170,100,.5),rgba(40,170,100,0)),
    radial-gradient(ellipse 400px 180px at 80% 20%,rgba(10,110,60,.5),rgba(10,110,60,0)),
    linear-gradient(180deg,#0f8447 0%,#149150 70%,#1c9a57 100%)}
.service-card{top:1099px;width:324px;height:383px;background:#fff}
.service-photo{width:324px;height:223px}
.service-title{top:280px;width:100%;text-align:center;font-family:'Poppins',sans-serif;font-size:18px;font-weight:400;color:var(--ink)}
.service-rule{left:28px;right:28px;top:334px;height:1px;background:var(--line)}
.service-link{top:351px;width:100%;text-align:center;font-size:10px;color:#888;letter-spacing:.5px}
.service-link.active{color:var(--green)}
.service-icon{left:143px;top:240px}

/* testimonials */
.quote{top:1724px;font-size:13px;font-style:italic;line-height:23px;color:#666}
.stars{top:1772px;color:#f39c12;font-size:16px;letter-spacing:3px}
.author{top:1803px;font-size:12px;font-weight:600;letter-spacing:.5px;color:#333}
.arrow-btn{width:38px;height:38px;border-radius:50%;border:1px solid #ccc;display:flex;align-items:center;justify-content:center;top:1711px}

/* staff */
.staff{top:1882px;left:0;width:1200px;height:603px;background:var(--staff-bg)}
.staff-card{top:2020px;width:324px;height:324px;overflow:hidden}
.staff-photo{left:0;top:0;width:324px;height:324px}
.staff-fade{left:0;right:0;bottom:0;height:150px;background:linear-gradient(180deg,rgba(0,0,0,0),rgba(0,0,0,.4))}
.staff-name{left:28px;font-family:'Poppins',sans-serif;font-size:22px;font-weight:300;color:#fff}
.staff-role{left:28px;font-size:12px;color:#fff}
.staff-arrow{left:280px;top:275px}
.social-dot{width:24px;height:24px;border-radius:50%;border:1px solid #fff}
.more-btn{left:518px;top:2384px;width:164px;height:45px;background:#e3efc6;color:var(--green);font-size:12px;display:flex;align-items:center;justify-content:center}

/* stats */
.stats{top:2485px;left:0;width:1200px;height:201px;
  background:
    radial-gradient(ellipse 300px 120px at 15% 40%,rgba(120,170,40,.45),rgba(120,170,40,0)),
    radial-gradient(ellipse 320px 140px at 88% 60%,rgba(110,160,40,.5),rgba(110,160,40,0)),
    linear-gradient(180deg,#a3cf45,#8cc33a)}
.stat{width:240px;text-align:center;color:#fff}
.stat-num{font-family:'Poppins',sans-serif;font-size:38px;font-weight:500;line-height:46px}
.stat-rule{width:40px;height:2px;background:#fff;margin:7px auto 10px}
.stat-label{font-family:'Poppins',sans-serif;font-size:17px;font-weight:300}

/* footer */
.footer{top:2686px;left:0;width:1200px;height:349px;background:var(--footer)}
.footer-bar{top:2986px;left:0;width:1200px;height:49px;background:var(--footer-bar)}
.footer-head{top:2750px;font-family:'Poppins',sans-serif;font-size:15px;font-weight:500;color:#fff}
.footer-text{left:89px;top:2786px;width:345px;font-size:12px;line-height:22px;color:#a9acb1}
.footer-mail{left:89px;top:2843px;font-size:12px;color:#fff;display:flex;align-items:center;gap:8px}
.pay-card{top:2882px;width:44px;height:28px;border-radius:3px;background:#fff}
.footer-links{top:2787px;list-style:none;font-size:12px;line-height:28.3px;color:#a9acb1}
.footer-links.social li{display:flex;align-items:center;gap:10px}
.footer-links .on{color:#fff}
.mini-dot{width:7px;height:7px;border-radius:50%;background:#a9acb1}
.copyright{top:3003px;font-size:11px;color:#8a8d92}
.to-top{left:1136px;top:2966px;width:40px;height:40px;border-radius:50%;background:var(--green);display:flex;align-items:center;justify-content:center}
</style>
</head>
<body>

<!-- hero -->
<section class="abs hero" role="img" aria-label="Photo of a uniformed cleaning professional in a bright interior"></section>
<div class="abs hero-shade"></div>
<div class="abs nav-mark"></div>
<div class="abs brand"><div class="brand-mark">Maple Ridge Solutions</div></div>
<nav class="abs nav">
  <a class="active" style="left:15px;top:0">Home</a>
  <a style="left:80px;top:0">About</a>
  <a style="left:142px;top:0">Contact</a>
  <a style="left:217px;top:0">Blogs</a>
</nav>
<div class="abs book-btn">Book Now</div>
<h1 class="abs center hero-title">Kingdom of Bahrain<br>Maple Ridge Solutions W.L.L</h1>
<div class="abs hero-btn">Learn More</div>
<span class="abs slide-dot" style="top:268px;background:var(--green)"></span>
<span class="abs slide-dot" style="top:286px"></span>
<span class="abs slide-dot" style="top:305px"></span>

<!-- process -->
<h2 class="abs center heading" style="top:636px">Our Process</h2>
<div class="abs heading-rule" style="top:674px"></div>

<svg class="abs" style="left:340px;top:760px" width="170" height="40" viewBox="0 0 170 40"><path d="M5 12 Q85 45 165 12" fill="none" stroke="#bbb" stroke-width="2" stroke-dasharray="2 6"/><path d="M158 8 l8 4 l-7 5" fill="none" stroke="#bbb" stroke-width="2"/></svg>
<svg class="abs" style="left:695px;top:760px" width="170" height="40" viewBox="0 0 170 40"><path d="M5 12 Q85 45 165 12" fill="none" stroke="#bbb" stroke-width="2" stroke-dasharray="2 6"/><path d="M158 8 l8 4 l-7 5" fill="none" stroke="#bbb" stroke-width="2"/></svg>

<div class="abs step-circle" style="left:195px;top:725px">
  <svg width="44" height="44" viewBox="0 0 44 44" fill="none" stroke="#8a9ab0" stroke-width="1.6"><rect x="4" y="8" width="36" height="32" rx="2"/><path d="M4 16h36M12 4v8M32 4v8M11 23h4M20 23h4M29 23h4M11 31h4M20 31h4M29 31h4"/></svg>
</div>
<div class="abs step-num" style="left:186px;top:731px">1</div>
<div class="abs step-circle" style="left:549px;top:725px">
  <svg width="44" height="44" viewBox="0 0 44 44" fill="none" stroke="#8cc53f" stroke-width="1.8"><path d="M22 3v16M14 19h16l4 20H10z"/><path d="M16 26v12M22 26v12M28 26v12"/></svg>
</div>
<div class="abs step-num" style="left:544px;top:731px">2</div>
<div class="abs step-circle" style="left:903px;top:725px">
  <svg width="44" height="44" viewBox="0 0 44 44" fill="none" stroke="#8a9ab0" stroke-width="1.6"><rect x="4" y="19" width="8" height="20"/><path d="M12 21l8-14c3 0 4 2 4 4l-2 8h12c2 0 4 2 3 4l-4 14c-1 2-2 2-4 2H12"/></svg>
</div>
<div class="abs step-num" style="left:898px;top:731px">3</div>

<h3 class="abs step-title" style="left:97px;top:845px">Book Staff</h3>
<h3 class="abs step-title" style="left:451px;top:845px">Get Service</h3>
<h3 class="abs step-title" style="left:805px;top:845px">Get Satisfied</h3>
<p class="abs step-text" style="left:97px;top:875px">Lorem ipsum dolor sit amet, consectetuer<br>elit. Aenean commodo ligula.</p>
<p class="abs step-text" style="left:451px;top:875px">Lorem ipsum dolor sit amet, consectetuer<br>elit. Aenean commodo ligula.</p>
<p class="abs step-text" style="left:805px;top:875px">Lorem ipsum dolor sit amet, consectetuer<br>elit. Aenean commodo ligula.</p>

<!-- services -->
<section class="abs services"></section>
<h2 class="abs center heading" style="top:1038px;color:#fff">Services we Provide</h2>
<div class="abs heading-rule" style="top:1076px"></div>

<article class="abs service-card" style="left:89px">
  <div class="service-photo" role="img" aria-label="Photo of a bright open-plan office with plants"
    style="background:radial-gradient(ellipse 70px 60px at 88% 55%,rgba(80,110,60,.7),rgba(80,110,60,0)),radial-gradient(ellipse 60px 50px at 10% 60%,rgba(80,110,60,.6),rgba(80,110,60,0)),linear-gradient(180deg,#f2f1ed 0%,#e4e3de 40%,#8b8983 62%,#5b5853 78%,#9a968e 100%)"></div>
  <svg class="abs service-icon" width="38" height="36" viewBox="0 0 38 36" fill="none" stroke="#8a9ab0" stroke-width="1.5"><path d="M4 35V12h10v23M14 35V4h12v31M26 35V16h8v19M2 35h34M18 9h4M18 15h4M18 21h4M7 18h4M7 24h4M29 22h2"/></svg>
  <h3 class="abs service-title">Office Cleaning</h3>
  <div class="abs service-rule"></div>
  <div class="abs service-link">+ VIEW SERVICE</div>
</article>
<article class="abs service-card" style="left:439px">
  <div class="service-photo" role="img" aria-label="Photo of a meeting room with a brick wall"
    style="background:radial-gradient(ellipse 90px 60px at 80% 35%,rgba(150,85,60,.75),rgba(150,85,60,0)),linear-gradient(180deg,#f4f3f0 0%,#e6e5e1 22%,#b5a796 40%,#5e6656 62%,#d9d2c2 78%,#e8e2d4 100%)"></div>
  <svg class="abs service-icon" width="38" height="36" viewBox="0 0 38 36" fill="none" stroke="#8cc53f" stroke-width="1.6"><path d="M8 4h16l-4 8H12zM16 12v6M12 18h10l-2 16h-6zM26 6l8-3M26 9l9 1M26 12l7 4"/></svg>
  <h3 class="abs service-title">Custom Cleaning</h3>
  <div class="abs service-rule"></div>
  <div class="abs service-link active">+ VIEW SERVICE</div>
</article>
<article class="abs service-card" style="left:787px">
  <div class="service-photo" role="img" aria-label="Photo of a stone government building entrance"
    style="background:radial-gradient(ellipse 40px 60px at 52% 62%,rgba(50,45,40,.8),rgba(50,45,40,0)),linear-gradient(180deg,#d9d5cc 0%,#c2bcb0 25%,#9e978b 50%,#6f6a62 72%,#8e8a83 88%,#a7a39c 100%)"></div>
  <svg class="abs service-icon" width="38" height="36" viewBox="0 0 38 36" fill="none" stroke="#8a9ab0" stroke-width="1.5"><path d="M4 10L19 3l15 7zM4 10h30M7 13v17M13 13v17M19 13v17M25 13v17M31 13v17M2 33h34M4 30h30"/></svg>
  <h3 class="abs service-title">Cleaning for Government</h3>
  <div class="abs service-rule"></div>
  <div class="abs service-link">+ VIEW SERVICE</div>
</article>

<!-- testimonials -->
<h2 class="abs center heading" style="top:1625px">Clients Testimonials</h2>
<div class="abs heading-rule" style="top:1662px"></div>
<div class="abs center" style="top:1676px;font-family:Georgia,serif;font-size:44px;line-height:44px;color:#ccc">&ldquo;</div>
<p class="abs center quote">&ldquo;Aenean vulputate eleifend tellus aenean leo ligula porttitor eu consequat vitae eleifend ac enim aliquam<br>lorem ante dapibus in viverra quis&rdquo;</p>
<div class="abs center stars">★★★★★</div>
<div class="abs center author">-MARTIN HALE</div>
<div class="abs arrow-btn" style="left:90px"><svg width="14" height="14" viewBox="0 0 14 14" fill="none" stroke="#777" stroke-width="1.5"><path d="M12 7H2M6 3L2 7l4 4"/></svg></div>
<div class="abs arrow-btn" style="left:1072px"><svg width="14" height="14" viewBox="0 0 14 14" fill="none" stroke="#777" stroke-width="1.5"><path d="M2 7h10M8 3l4 4-4 4"/></svg></div>

<!-- staff -->
<section class="abs staff"></section>
<h2 class="abs center heading" style="top:1945px">Our Staff Members</h2>
<div class="abs heading-rule" style="top:1982px"></div>

<article class="abs staff-card" style="left:89px">
  <div class="abs staff-photo" role="img" aria-label="Portrait photo of staff member Nora Vale"
    style="background:radial-gradient(ellipse 110px 150px at 58% 70%,rgba(140,200,185,.85),rgba(140,200,185,0)),radial-gradient(ellipse 80px 90px at 55% 25%,rgba(120,80,55,.55),rgba(120,80,55,0)),linear-gradient(100deg,#e9ece9 0%,#d3d8d4 35%,#eceae4 60%,#b8b5ad 100%)"></div>
  <div class="abs staff-fade"></div>
  <h3 class="abs staff-name" style="top:242px">Nora Vale</h3>
  <p class="abs staff-role" style="top:276px">Cleaner at Maple Ridge Solutions</p>
  <svg class="abs staff-arrow" width="16" height="14" viewBox="0 0 16 14" fill="none" stroke="#fff" stroke-width="1.5"><path d="M1 7h13M9 2l5 5-5 5"/></svg>
</article>
<article class="abs staff-card" style="left:439px">
  <div class="abs staff-photo" role="img" aria-label="Photo of staff member Eli Brandt at a glass building facade"
    style="background:radial-gradient(ellipse 90px 120px at 45% 45%,rgba(150,170,200,.55),rgba(150,170,200,0)),linear-gradient(120deg,#4d79bf 0%,#2c4f8f 35%,#3c64a8 55%,#1c3264 80%,#13244a 100%)"></div>
  <div class="abs staff-fade"></div>
  <h3 class="abs staff-name" style="top:195px">Eli Brandt</h3>
  <p class="abs staff-role" style="top:229px">Cleaner at Maple Ridge Solutions</p>
  <span class="abs social-dot" style="left:28px;top:263px"></span>
  <span class="abs social-dot" style="left:59px;top:263px;background:#29a9e1;border-color:#29a9e1"></span>
  <span class="abs social-dot" style="left:90px;top:263px"></span>
  <svg class="abs staff-arrow" width="16" height="14" viewBox="0 0 16 14" fill="none" stroke="#fff" stroke-width="1.5"><path d="M1 7h13M9 2l5 5-5 5"/></svg>
</article>
<article class="abs staff-card" style="left:787px">
  <div class="abs staff-photo" role="img" aria-label="Portrait photo of staff member Clara Wynn"
    style="background:radial-gradient(ellipse 150px 130px at 60% 85%,rgba(205,35,40,.95),rgba(205,35,40,0)),radial-gradient(ellipse 60px 70px at 25% 60%,rgba(230,120,40,.7),rgba(230,120,40,0)),linear-gradient(100deg,#b89a78 0%,#d6c3a6 35%,#c9a98a 65%,#a7784f 100%)"></div>
  <div class="abs staff-fade"></div>
  <h3 class="abs staff-name" style="top:242px">Clara Wynn</h3>
  <p class="abs staff-role" style="top:276px">Cleaner at Maple Ridge Solutions</p>
  <svg class="abs staff-arrow" width="16" height="14" viewBox="0 0 16 14" fill="none" stroke="#fff" stroke-width="1.5"><path d="M1 7h13M9 2l5 5-5 5"/></svg>
</article>
<div class="abs more-btn">More Staff members</div>

<!-- stats -->
<section class="abs stats" role="img" aria-label="Faint photo of an office interior in green tint"></section>
<div class="abs stat" style="left:139px;top:2536px"><div class="stat-num">360</div><div class="stat-rule"></div><div class="stat-label">Total Clients</div></div>
<div class="abs stat" style="left:479px;top:2536px"><div class="stat-num">350</div><div class="stat-rule"></div><div class="stat-label">Satisfied Clients</div></div>
<div class="abs stat" style="left:821px;top:2536px"><div class="stat-num">30</div><div class="stat-rule"></div><div class="stat-label">Total Staff</div></div>

<!-- footer -->
<footer class="abs footer"></footer>
<div class="abs footer-bar"></div>
<h4 class="abs footer-head" style="left:89px">About Us</h4>
<h4 class="abs footer-head" style="left:488px">Information</h4>
<h4 class="abs footer-head" style="left:721px">My Account</h4>
<h4 class="abs footer-head" style="left:941px">Follow us</h4>
<p class="abs footer-text">Lorem ipsum dolor sit amet, consectetuer adipiscing elit aenean commodo ligula eget dolor aenean massa.</p>
<div class="abs footer-mail"><svg width="12" height="9" viewBox="0 0 12 9"><rect width="12" height="9" fill="#fff"/><path d="M0 0l6 5 6-5" fill="none" stroke="#1e2024"/></svg>info@mapleridgesolutions.com</div>
<span class="abs pay-card" style="left:89px"></span>
<span class="abs pay-card" style="left:140px;background:#2a3a9a"></span>
<span class="abs pay-card" style="left:189px;background:#1e2024;border:1px solid #444"></span>
<span class="abs pay-card" style="left:240px"></span>

<ul class="abs footer-links" style="left:488px"><li>About us</li><li>Sitemap</li><li>Advanced Search</li><li>Bookings and Returns</li><li>Contact</li></ul>
<ul class="abs footer-links" style="left:721px"><li>Log In</li><li>History</li><li>Account</li><li>Track My Order</li><li>Help</li></ul>
<ul class="abs footer-links social" style="left:941px">
  <li><span class="mini-dot"></span>Linkway</li>
  <li class="on"><span class="mini-dot" style="background:var(--green)"></span>Chirpline</li>
  <li><span class="mini-dot"></span>Circlepost</li>
  <li><span class="mini-dot"></span>Snapframe</li>
</ul>
<p class="abs center copyright">© 2017. All Rights Reserved.</p>
<div class="abs to-top"><svg width="12" height="14" viewBox="0 0 12 14" fill="none" stroke="#fff" stroke-width="1.6"><path d="M6 13V2M1 6l5-5 5 5"/></svg></div>

</body>
</html>
```